Free Offer Book Cover

I am creating a funnel page where I offer a free download of a PDF called. Twelve-Week Launch Kit. A road map for new leaders. I have included samples of other book covers. It can look like a book, or a checklist, or something that illustrates what they are getting. Bright Harbor Coaching is the company if you could get the logo into the book cover as well.

Target Market(s)

New leaders, young professionals

Font styles to use
Sans Serif

Requirements
Must have
• Name of content. Twelve-Week Launch Kit for new leaders.

```html
<!DOCTYPE html>
<html lang="en">
<head>
<meta charset="utf-8">
<title>Twelve-Week Launch Kit — Cover</title>
<link rel="stylesheet" href="https://fonts.googleapis.com/css2?family=Arimo:wght@700&display=swap">
<style>
  :root {
    --page: #ffffff;
    --cover: #000000;
    --frame: #0f2340;
    --banner: #b3bfcd;
    --ink-navy: #16233a;
    --tab: #1a2a42;
    --label: #bcc6d3;
    --rule: #c9d1dc;
    --brand-red: #c3161c;
    --glow: rgba(24, 40, 70, 0.45);
  }
  * { box-sizing: border-box; margin: 0; padding: 0; }
  html, body {
    width: 1200px; height: 1200px; overflow: hidden;
    background: var(--page);
    font-family: "Arimo", Arial, sans-serif;
  }
  .cover {
    position: absolute; left: 200px; top: 60px;
    width: 800px; height: 1080px;
    background: var(--cover);
    overflow: hidden;
  }
  .cover-glow {
    position: absolute; right: -90px; bottom: -60px;
    width: 440px; height: 440px; border-radius: 50%;
    background: radial-gradient(circle, var(--glow) 0%, rgba(24,40,70,0.15) 60%, rgba(0,0,0,0) 72%);
  }
  .cover-art { position: absolute; inset: 0; }
  .title-band {
    position: absolute; left: 40px; top: 250px;
    width: 690px; height: 92px;
    background: var(--banner);
    display: flex; align-items: center; justify-content: center;
  }
  .title {
    color: var(--ink-navy);
    font-weight: 700; font-size: 45px;
    letter-spacing: 0.5px; white-space: nowrap;
  }
  .subtitle-tab {
    position: absolute; left: 220px; top: 342px;
    width: 510px; height: 66px;
    background: var(--tab);
    clip-path: polygon(22px 0, 100% 0, 100% 100%, 0 100%);
    display: flex; align-items: center; justify-content: flex-end;
    padding-right: 20px; gap: 16px;
  }
  .subtitle-rule { width: 90px; height: 3px; background: #ffffff; }
  .subtitle {
    color: #ffffff; font-weight: 700; font-size: 38px; white-space: nowrap;
  }
  .plan-label {
    position: absolute; left: 100px;
    color: var(--label); font-weight: 700; font-size: 42px;
  }
  .brand {
    position: absolute; right: 95px; bottom: 120px;
    color: var(--brand-red); font-weight: 700; font-size: 34px;
    line-height: 1.05; text-align: right; width: 260px;
  }
</style>
</head>
<body>
  <div class="cover">
    <div class="cover-glow"></div>
    <svg class="cover-art" width="800" height="1080" viewBox="0 0 800 1080" aria-hidden="true">
      <path d="M80 50 H720 A30 30 0 0 0 750 80 V1000 A30 30 0 0 0 720 1030 H80 A30 30 0 0 0 50 1000 V80 A30 30 0 0 0 80 50 Z"
            fill="none" stroke="var(--frame)" stroke-width="7"/>
      <g stroke="var(--rule)" stroke-width="3" stroke-dasharray="22 5 3 5">
        <line x1="240" y1="545" x2="725" y2="545"/>
        <line x1="240" y1="632" x2="725" y2="632"/>
        <line x1="240" y1="716" x2="725" y2="716"/>
        <line x1="240" y1="800" x2="725" y2="800"/>
        <line x1="240" y1="888" x2="725" y2="888"/>
      </g>
    </svg>

    <div class="title-band"><h1 class="title">TWELVE-WEEK LAUNCH KIT</h1></div>
    <div class="subtitle-tab"><span class="subtitle-rule"></span><p class="subtitle">for new leaders.</p></div>

    <p class="plan-label" style="top:500px">WHO</p>
    <p class="plan-label" style="top:588px">WHAT</p>
    <p class="plan-label" style="top:672px">HOW</p>
    <p class="plan-label" style="top:756px">WHEN</p>

    <p class="brand">Bright Harbor Coaching</p>
  </div>
</body>
</html>
```